Coral Voyage Mate - A Travel Services Website

Islestay Cottage Rentals is a company that provides travels services to home owners and travellers to Barbados. Coral Voyage Mate is a particular brand targeting travelling guests with specific set of travel services. The brand slogan is:

'Getting you the best for less'

The travel services will include:

- Coral Voyage Mate Perk Pass
- Car Hire Quote Service
- Mobile Phone Sim Cards
- Prepaid Debit Cards
- Airport Hotel Booking
- Airport Lounge Booking
- Airport Parking

There will also be a travel planner function for guests.

The main puropse of the site is as follows:

1. Registration for the Coral Voyage Mate Perk Pass

2. Creation of user account which the guest will frequently return to check for updates

3. Purchase of ancillary travel products and services

4. To use the Travel Planner

5. To gather data on holiday home owners in Barbados

A site map can be seen at the following link:

http://plotgrid-example.com/charts/viewChart/4kqzvb8ynhpwe2ufa6rj0xmc51tlsg9odiq3ye70bnc8hva2wk

Webpage templates (2 required)

The first will be form control heavy (text boxes, checkboxes ect). It will need failure and success messages / indicators etc.

The second will be a general content area with a secondary navigation area (i.e for sub sections of the current section). This will house text / headings and images.

Both will require header, primary navigation, content and footer areas.

N.B. Please not that I am not technical and the above webtemplate narrative has been supplied by my web developer/programmer. If you have any questions, please ask me any questions and I will get an answer from him.

Target Market(s)

My customers tend to be:

Sex: Female
Age: 24-55
Location: UK, USA, Canada
Social Class: A,B,C1
Income: Medium income bracket

They are possibly visiting Barbados for the first and only time. It is an expensive destination and is accessible to people with a medium to high income. They still desire 'value for money'. Therefore the sight must give guests confidence that Coral Voyage Mate is 'their friend', is seeking to offer the best value deals for their vacation/holiday.

Industry/Entity Type

Travel

Requirements
Must have
• The site templates must be professional, aspirational, trustworthy, reassuring, clean, innovative, fun. When people visit the site they should be excited about the savings that they can make and want to return as there is a perceived benefit for them. It must look expensive and professional in its projected image.
Nice to have
• Smooth currved lines, seperated boxed areas for content, as simple and uncluttered layout and it must be simple to read!
Should not have
• It should not be cartoonly, despite my attached logo and must not look cheap.

```html
<!DOCTYPE html>
<html lang="en">
<head>
<meta charset="utf-8">
<title>Coral Voyage Mate – Getting you the best for less</title>
<link rel="stylesheet" href="https://fonts.googleapis.com/css2?family=Caveat+Brush&family=Caveat:wght@600&family=Arimo&display=swap">
<style>
  :root{
    --sky-top:#2f7fd6;
    --sky-mid:#9fcdf0;
    --sea:#7fd8d8;
    --sand:#efdca2;
    --sand-deep:#e2c77e;
    --panel:rgba(240,246,255,.86);
    --header-wash:rgba(205,222,248,.9);
    --nav-blue:#0e46b8;
    --nav-line:#6fb4ff;
    --logo-red:#e0101d;
    --wood:#a8753f;
    --rope:#1d1a16;
    --ink:#2a1a12;
    --welcome:#f26a12;
    --body-text:#3a3a3a;
    --slogan:#0c2fd0;
    --note:#f0b95a;
    --tape:rgba(150,120,60,.75);
    --shop-blue:#0a45c8;
    --white:#ffffff;
  }
  *{box-sizing:border-box;margin:0;padding:0}
  html,body{width:1200px;height:990px;overflow:hidden}
  body{position:relative;font-family:"Arimo",Arial,sans-serif}
  a{text-decoration:none}
  .beach-backdrop{position:absolute;inset:0;
    background:linear-gradient(180deg,var(--sky-top) 0%,var(--sky-mid) 45%,var(--sea) 58%,var(--sea) 64%,var(--sand) 72%,var(--sand-deep) 100%)}
  .page{position:absolute;left:117px;top:72px;width:965px;height:845px;background:var(--panel)}
  .site-header{position:absolute;left:0;top:0;width:100%;height:201px;background:var(--header-wash)}
  .brand{position:absolute;left:48px;top:78px;display:flex;align-items:center;gap:18px}
  .brand-dot{width:70px;height:70px;border-radius:50%;background:var(--logo-red)}
  .brand-name{font-family:"Caveat Brush",cursive;font-size:60px;color:var(--logo-red);line-height:1}
  .primary-nav{position:absolute;left:0;top:201px;width:100%;height:47px;
    background:linear-gradient(180deg,#0a3aa8,var(--nav-blue) 70%,#3a7be0);
    display:flex;align-items:center;padding-left:27px}
  .primary-nav a{font-family:"Caveat Brush",cursive;color:var(--white);font-size:18px;
    padding:0 7px;border-left:1px solid var(--nav-line);line-height:26px;white-space:nowrap}
  .primary-nav a:first-child{border-left:0;padding-left:0}
  .service-signs{position:absolute;left:35px;top:272px;width:176px;height:545px}
  .service-signs .rope{position:absolute;top:20px;width:5px;height:500px;background:repeating-linear-gradient(180deg,var(--rope) 0 9px,transparent 9px 13px)}
  .service-signs a{position:absolute;left:0;width:176px;height:50px;background:linear-gradient(180deg,#c08a52,var(--wood) 60%,#8a5a2e);
    border-radius:4px;box-shadow:0 3px 4px rgba(0,0,0,.3);font-family:"Caveat Brush",cursive;font-size:25px;
    color:var(--ink);padding-left:16px;line-height:48px;white-space:nowrap}
  .hero{position:absolute;left:231px;top:273px;width:448px;height:247px;border-radius:14px;overflow:hidden;
    background:linear-gradient(180deg,#3fc7f0 0%,#8fe0f2 60%,#5cc3d8 100%)}
  .hero-photo{position:absolute;right:20px;top:10px;width:250px;height:237px;
    background:radial-gradient(ellipse at 50% 55%,rgba(255,255,255,.75),rgba(230,200,170,.35) 55%,transparent 75%)}
  .slogan{position:absolute;left:18px;top:24px;font-family:"Caveat",cursive;font-weight:600;font-size:33px;line-height:34px;color:var(--slogan)}
  .welcome{position:absolute;left:235px;top:540px;width:410px}
  .welcome h1{font-family:"Caveat Brush",cursive;font-weight:400;font-size:50px;color:var(--welcome);line-height:1}
  .welcome p{margin-top:14px;font-size:16px;line-height:20.4px;color:var(--body-text)}
  .planner-note{position:absolute;left:748px;top:293px;width:170px;height:142px;background:var(--note);transform:rotate(2deg);
    box-shadow:0 3px 6px rgba(0,0,0,.25);font-family:"Caveat Brush",cursive;font-size:40px;line-height:38px;color:var(--ink);padding:42px 0 0 32px}
  .tape{position:absolute;top:-18px;width:20px;height:52px;background:var(--tape)}
  .polaroid{position:absolute;background:var(--white);box-shadow:0 3px 8px rgba(0,0,0,.3);padding:12px 12px 0}
  .polaroid .shot{width:100%;border:6px solid #111}
  .polaroid span{display:block;font-family:"Caveat Brush",cursive;font-size:30px;color:var(--ink);text-align:center;line-height:36px;white-space:nowrap}
  .pin{position:absolute;width:14px;height:14px;border-radius:50%;background:#ee5a16}
  .video-card{left:678px;top:540px;width:165px;height:160px;transform:rotate(-8deg)}
  .video-card .shot{height:112px;background:linear-gradient(160deg,#1c8fa0,#4fc0a8 50%,#9a8a2a)}
  .gallery-card{left:770px;top:420px;width:172px;height:180px;transform:rotate(16deg)}
  .gallery-card .shot{height:128px;background:linear-gradient(160deg,#3ab4e8,#f06a8a 50%,#d23a3a)}
  .shop-button{position:absolute;left:691px;top:714px;width:252px;height:118px}
  .shop-button .shop-panel{position:absolute;left:90px;top:8px;right:0;bottom:4px;border-radius:16px;
    background:linear-gradient(90deg,#2a6ad8,var(--shop-blue));box-shadow:0 2px 5px rgba(0,0,0,.3)}
  .shop-button .shop-photo{position:absolute;left:0;top:0;width:118px;height:118px;border-radius:50%;
    background:radial-gradient(circle at 50% 40%,#e6f6ff,#62d8f0 60%,#3ec6e6)}
  .shop-button b{position:absolute;left:140px;top:30px;font-family:"Caveat Brush",cursive;font-weight:400;font-size:52px;color:var(--white);line-height:1}
</style>
</head>
<body>
  <div class="beach-backdrop" role="img" aria-label="Tropical beach with palm tree, turquoise sea and golden sand"></div>

  <div class="page">
    <header class="site-header">
      <div class="brand">
        <span class="brand-dot"></span>
        <span class="brand-name">Coral Voyage Mate</span>
      </div>
    </header>

    <nav class="primary-nav">
      <a href="#">Perk Pass Club</a>
      <a href="#">Benefit Blogs</a>
      <a href="#">Testimonials</a>
      <a href="#">Travel Planner</a>
      <a href="#">Free Resources</a>
      <a href="#">Travel News</a>
      <a href="#">Shop</a>
      <a href="#">Affiliate Join Us Form</a>
      <a href="#">A Poll</a>
    </nav>

    <div class="service-signs">
      <span class="rope" style="left:38px"></span>
      <span class="rope" style="left:134px"></span>
      <a href="#" style="top:0">airport parking</a>
      <a href="#" style="top:72px">airport hotel</a>
      <a href="#" style="top:145px">airport lounge</a>
      <a href="#" style="top:217px">car hire</a>
      <a href="#" style="top:295px">attractions</a>
      <a href="#" style="top:363px">travel money</a>
      <a href="#" style="top:430px">mobile simcards</a>
      <a href="#" style="top:495px">privilege cards</a>
    </div>

    <section class="hero">
      <div class="hero-photo" role="img" aria-label="Family of four running along the shoreline"></div>
      <p class="slogan">Getting you the best<br>for less</p>
    </section>

    <section class="welcome">
      <h1>welcome</h1>
      <p>Lorem ipsum dolor sit amet, consectetur adipiscing elit. Aliquam ipsum est, viverra in egestas a, pulvinar vitae erat. Nam libero mi, aliquet eget feugiat non, volutpat pretium dui. Suspendisse porta ultrices bibendum. Nam leo lorem, molestie id blandit sed, feugiat in purus. Sed ac eros in velit faucibus fringilla. Nam orci elit, malesuada nec ultrices vel, rutrum quis massa.</p>
    </section>

    <a class="planner-note" href="#">
      <span class="tape" style="left:28px;transform:rotate(-4deg)"></span>
      <span class="tape" style="left:132px;transform:rotate(14deg)"></span>
      travel<br>planner
    </a>

    <a class="polaroid video-card" href="#">
      <div class="shot" role="img" aria-label="Underwater reef with starfish"></div>
      <span>video</span>
    </a>
    <a class="polaroid gallery-card" href="#">
      <div class="shot" role="img" aria-label="Friends in snorkel masks on holiday"></div>
      <span>photo gallery</span>
    </a>
    <span class="pin" style="left:868px;top:420px"></span>
    <span class="pin" style="left:760px;top:530px"></span>

    <a class="shop-button" href="#">
      <span class="shop-panel"></span>
      <span class="shop-photo" role="img" aria-label="Woman in sun hat relaxing on the beach"></span>
      <b>Shop</b>
    </a>
  </div>
</body>
</html>
```